Capital Management company needs a web design

We have a domain name and logo but need hosting and design. Please look at the Must-Haves section.

Target Market(s)

banking industry and investors

Industry/Entity Type

Investment

Coding

Coded - Design and coding required

Number of Pages Required

1 page

Font styles to use
Sans Serif

Requirements
Must have
• Picture(s) of skyscraper skyline (can be of Manhattan, Chicago, or any other major city in the USA).
• Please use the three colors of the logo as a backdrop to part of the webpage(s)
Should not have
• No "what our clients say" section
• No pictures of people

```html
<!DOCTYPE html>
<html lang="en">
<head>
<meta charset="utf-8">
<title>Harbor Crest Capital – Home and Strategy Pages</title>
<link href="https://fonts.googleapis.com/css2?family=Raleway:wght@300;400;500;700&family=Roboto:wght@400;500;700&display=swap" rel="stylesheet">
<style>
:root{
  --blue:#1a73c1;
  --blue-dark:#0f5a9c;
  --ink:#1d1d1d;
  --text:#555a60;
  --muted:#8a8f95;
  --line:#e3e6ea;
  --panel:#f2f3f5;
  --band:#f6f7f8;
  --white:#ffffff;
  --page:#ffffff;
}
*{margin:0;padding:0;box-sizing:border-box}
html,body{width:671px;height:1200px;overflow:hidden;background:var(--page)}
body{position:relative;font-family:"Roboto",Arial,sans-serif;color:var(--text)}

.board-title{position:absolute;left:0;width:671px;text-align:center;font-family:"Raleway",Arial,sans-serif;font-weight:400;font-size:23px;color:var(--ink);letter-spacing:.3px}
.board-title.home{top:28px}
.board-title.strategy{top:323px}

.page{position:absolute;left:115px;width:448px;background:var(--white);box-shadow:0 0 6px rgba(0,0,0,.12);overflow:hidden}
.page.home{top:70px;height:224px}
.page.strategy{top:373px;height:793px}

/* header */
.site-header{position:absolute;left:0;top:0;width:100%;height:26px;z-index:3}
.brand{position:absolute;left:0;top:0;width:86px;height:26px;background:var(--white);display:flex;align-items:center;gap:4px;padding-left:7px}
.brand-mark{width:6px;height:6px;border-radius:50%;background:var(--blue)}
.brand-name{font-family:"Roboto",Arial,sans-serif;font-weight:700;font-size:6.4px;color:var(--blue);letter-spacing:.1px;white-space:nowrap}
.main-nav{position:absolute;left:104px;top:10px;display:flex;gap:11px}
.main-nav a{font-size:4px;color:var(--white);text-decoration:none;font-weight:500;white-space:nowrap}
.main-nav a.active{border-bottom:1px solid var(--white);padding-bottom:2px}
.login{position:absolute;right:9px;top:9px;height:8px;padding:0 4px;border-radius:4px;background:var(--white);color:var(--blue);font-size:3.8px;font-weight:700;display:flex;align-items:center;gap:2px}
.login svg{width:4px;height:4px}

/* home hero */
.home-hero{position:absolute;left:0;top:0;width:100%;height:214px;background:
  radial-gradient(ellipse at 50% 60%,rgba(214,128,52,.45),transparent 60%),
  linear-gradient(180deg,#3d4654 0%,#2a2c30 25%,#3a2a1c 55%,#1f1813 100%)}
.hero-copy{position:absolute;left:0;top:82px;width:100%;text-align:center;color:var(--white)}
.hero-copy h1{font-family:"Raleway",Arial,sans-serif;font-weight:300;font-size:11.5px;margin-bottom:5px}
.hero-copy p{font-size:4.6px;line-height:7.6px;width:205px;margin:0 auto}
.btn-contact{display:inline-block;margin-top:7px;height:9px;padding:0 8px;border-radius:5px;background:var(--white);color:var(--blue);font-size:3.6px;font-weight:700;line-height:9px}

.site-footer{position:absolute;left:0;bottom:0;width:100%;height:10px;background:var(--blue);color:var(--white);font-size:3.6px;display:flex;align-items:center;padding-left:80px;gap:3px;white-space:nowrap}
.site-footer .dot{width:2px;height:2px;border-radius:50%;background:var(--white)}

/* strategy hero */
.strategy-hero{position:absolute;left:0;top:0;width:100%;height:154px;background:
  radial-gradient(ellipse at 45% 25%,rgba(238,176,86,.75),transparent 55%),
  linear-gradient(180deg,#6b5238 0%,#a07744 28%,#6f5a44 50%,#3f3a36 75%,#2b2a2a 100%)}
.strategy-hero h1{position:absolute;top:70px;width:100%;text-align:center;font-family:"Raleway",Arial,sans-serif;font-weight:300;font-size:11px;color:var(--white)}

.section-head{position:absolute;top:172px;width:100%;text-align:center}
.section-head h2{font-family:"Roboto",Arial,sans-serif;font-weight:700;font-size:10.4px;color:var(--ink)}
.section-head h2 span{color:var(--blue)}
.section-head p{margin-top:5px;font-size:5.4px;color:var(--muted)}

.side-menu{position:absolute;left:63px;top:215px;width:73px;list-style:none}
.side-menu li{height:15px;border-bottom:1px solid var(--line);font-size:3.8px;font-weight:500;color:var(--ink);padding-left:3px;line-height:14px;text-transform:uppercase}
.side-menu li.active{height:11px;line-height:11px;margin-bottom:3px;color:var(--white);background:linear-gradient(90deg,var(--blue) 0%,var(--blue) 55%,rgba(26,115,193,0) 100%);border-bottom:none}

.article{position:absolute;left:144px;top:213px;width:160px;font-size:3.9px;line-height:7.8px;color:var(--text)}
.article p{margin-bottom:5px}
.points{list-style:none;margin-top:8px}
.points li{position:relative;padding-left:9px;margin-bottom:5px}
.points li::before{content:"";position:absolute;left:0;top:2.6px;width:3px;height:3px;border-radius:50%;background:var(--blue)}
.points b{color:var(--ink);font-weight:700}

.video{position:absolute;left:144px;top:525px;width:160px;height:97px;background:linear-gradient(135deg,#c8ccd2 0%,#e6e8ec 45%,#9fb2c8 75%,#5a7aa3 100%)}
.video svg{position:absolute;left:69px;top:37px}

.aside-note{position:absolute;left:312px;top:213px;width:75px;height:118px;background:var(--panel);padding:8px 8px;font-size:4.7px;line-height:9.8px;color:var(--text)}
.ad{position:absolute;left:312px;width:75px;height:70px;background:var(--panel)}
.ad.one{top:337px}
.ad.two{top:412px}
.ad svg{position:absolute;left:0;top:0}
.ad span{position:absolute;width:100%;top:32px;text-align:center;font-size:4.4px;color:var(--muted);letter-spacing:.2px}

.topics-band{position:absolute;left:0;top:671px;width:100%;height:110px;background:var(--band)}
.topic-card{position:absolute;top:657px;width:75px;height:102px;background:var(--white);box-shadow:0 1px 3px rgba(0,0,0,.12);text-align:center}
.topic-card .thumb{height:56px}
.topic-card .icon{position:absolute;left:32px;top:51px;width:11px;height:11px;border-radius:50%;background:var(--white);display:flex;align-items:center;justify-content:center}
.topic-card h3{margin-top:11px;font-size:4.6px;font-weight:700;color:var(--blue);text-transform:uppercase}
.topic-card p{margin:3px auto 0;width:64px;font-size:3.9px;line-height:6.6px;color:var(--text)}
.c1{left:62px}.c2{left:145px}.c3{left:229px}.c4{left:312px}
.c1 .thumb{background:linear-gradient(135deg,#7d8a6d,#c9c2a4 50%,#5b5f52)}
.c2 .thumb{background:linear-gradient(135deg,#1a1f2a,#2c4c7a 55%,#4f86c6)}
.c3 .thumb{background:linear-gradient(135deg,#e9ecef,#c3c9cf 50%,#8a96a3)}
.c4 .thumb{background:linear-gradient(135deg,#c9b7a1,#e8dfd3 45%,#9b3b33 80%,#d7d2cc)}
.strategy .site-footer{padding-left:78px}
</style>
</head>
<body>

<h2 class="board-title home">Home Page</h2>

<section class="page home">
  <div class="home-hero" role="img" aria-label="Night aerial view of a city skyline of skyscrapers with warm lights"></div>
  <header class="site-header">
    <div class="brand"><span class="brand-mark"></span><span class="brand-name">Harbor Crest Capital</span></div>
    <nav class="main-nav">
      <a class="active" href="#">Home</a><a href="#">Strategy</a><a href="#">Our Team</a><a href="#">Services</a><a href="#">News &amp; Insights</a><a href="#">About Us</a><a href="#">Contact</a>
    </nav>
    <div class="login"><svg viewBox="0 0 8 8"><rect x="1" y="1" width="6" height="6" fill="none" stroke="#1a73c1" stroke-width="1"/><path d="M2 4h4M4.5 2.5 6 4 4.5 5.5" fill="none" stroke="#1a73c1" stroke-width="1"/></svg>LOGIN</div>
  </header>
  <div class="hero-copy">
    <h1>Experience the power of us</h1>
    <p>Lorem ipsum dolor sit amet, consectetur adipiscing elit, sed do eiusmod tempor incididunt ut labore et dolore magna aliqua. Ut enim ad minim veniam, quis nostrud exercitation ullamco laboris</p>
    <span class="btn-contact">CONTACT US</span>
  </div>
  <footer class="site-footer">
    <span>© 2019 Harbor Crest Capital</span><span class="dot"></span><span>All rights reserved</span><span class="dot"></span><span>48 Meridian Row, Suite 9, Lakeport, IL 60000</span><span class="dot"></span><span>(555) 010 - 2040</span>
  </footer>
</section>

<h2 class="board-title strategy">Strategy Page</h2>

<section class="page strategy">
  <div class="strategy-hero" role="img" aria-label="City skyline of skyscrapers at sunset with a tall spire tower">
    <h1>Best Investing Strategies</h1>
  </div>
  <header class="site-header">
    <div class="brand"><span class="brand-mark"></span><span class="brand-name">Harbor Crest Capital</span></div>
    <nav class="main-nav">
      <a class="active" href="#">Home</a><a href="#">Strategy</a><a href="#">Our Team</a><a href="#">Services</a><a href="#">News &amp; Insights</a><a href="#">About Us</a><a href="#">Contact</a>
    </nav>
    <div class="login"><svg viewBox="0 0 8 8"><rect x="1" y="1" width="6" height="6" fill="none" stroke="#1a73c1" stroke-width="1"/><path d="M2 4h4M4.5 2.5 6 4 4.5 5.5" fill="none" stroke="#1a73c1" stroke-width="1"/></svg>LOGIN</div>
  </header>

  <div class="section-head">
    <h2>Our Investment <span>Strategy</span></h2>
    <p>Lorem ipsum dolor sit amet, consectetur adipiscing elit, sed do eiusmod tempor</p>
  </div>

  <ul class="side-menu">
    <li class="active">Basics</li>
    <li>Where to invest</li>
    <li>Types of investment</li>
    <li>Best investment strategies</li>
    <li>Taxation</li>
  </ul>

  <article class="article">
    <p>Lorem ipsum dolor sit amet, consectetur adipiscing elit, sed do eiusmod tempor incididunt ut labore et dolore magna aliqua. Ut enim ad minim veniam, quis nostrud exercitation ullamco laboris nisi ut aliquip ex ea commodo consequat. Duis aute irure dolor in reprehenderit in voluptate velit esse cillum dolore eu fugiat nulla pariatur. Excepteur sint occaecat cupidatat non proident, sunt in culpa qui officia deserunt mollit anim id est laborum.</p>
    <p>Sed ut perspiciatis unde omnis iste natus error sit voluptatem accusantium doloremque laudantium, totam rem aperiam, eaque ipsa quae ab illo inventore veritatis et quasi architecto beatae vitae dicta sunt explicabo. Nemo enim ipsam voluptatem quia voluptas sit aspernatur aut odit aut fugit, sed quia consequuntur magni dolores eos qui ratione voluptatem sequi nesciunt. Neque porro quisquam est, qui dolorem ipsum quia dolor sit amet, consectetur, adipisci velit, sed quia non numquam eius modi tempora incidunt ut labore et dolore magnam aliquam quaerat voluptatem.</p>
    <p>Ut enim ad minima veniam, quis nostrum exercitationem ullam corporis suscipit laboriosam, nisi ut aliquid ex ea commodi consequatur? Quis autem vel eum iure reprehenderit qui in ea voluptate velit esse quam nihil molestiae consequatur, vel illum qui dolorem eum fugiat quo voluptas nulla pariatur.</p>
    <ul class="points">
      <li><b>Lorem ipsum dolor sit amet</b> | consectetur adipiscing elit, sed do eiusmod tempor incididunt ut labore et dolore magna aliqua.</li>
      <li><b>Lorem ipsum dolor sit amet</b> | At vero eos et accusamus et iusto odio dignissimos ducimus qui blanditiis praesentium voluptatum deleniti atque corrupti quos dolores et quas molestias excepturi.</li>
      <li><b>Lorem ipsum dolor sit amet</b> | sint occaecati cupiditate non provident, similique sunt in culpa qui officia deserunt mollitia animi, id est laborum et dolorum fuga. Et harum quidem rerum facilis est et expedita distinctio. Nam libero tempore, cum soluta nobis est eligendi optio cumque nihil impedit quo.</li>
      <li><b>Lorem ipsum dolor sit amet</b> | consectetur adipiscing elit, sed do eiusmod tempor incididunt ut labore et dolore magna aliqua.</li>
      <li><b>Lorem ipsum dolor sit amet</b> | Et harum quidem rerum facilis est et expedita distinctio. Nam libero tempore, cum soluta nobis est eligendi.</li>
      <li><b>Lorem ipsum dolor sit amet</b> | Quidem rerum facilis est et expedita distinctio. Nam libero tempore, cum soluta nobis.</li>
    </ul>
  </article>

  <div class="video" role="img" aria-label="Video still of hands working with a calculator over printed financial charts">
    <svg width="22" height="22" viewBox="0 0 22 22"><circle cx="11" cy="11" r="9.5" fill="none" stroke="#ffffff" stroke-width="1.3"/><path d="M9 7v8l6-4z" fill="none" stroke="#ffffff" stroke-width="1.2" stroke-linejoin="round"/></svg>
  </div>

  <aside class="aside-note">Nam libero tempore, cum soluta nobis est eligendi optio cumque nihil impedit quo minus id quod maxime placeat facere possimus, omnis voluptas assumenda est, omnis dolor repellendus. Temporibus autem quibusdam et aut officiis debitis aut rerum.</aside>
  <div class="ad one"><svg width="75" height="70" viewBox="0 0 75 70"><path d="M0 0L75 70M75 0L0 70" stroke="#e3e5e8" stroke-width=".8"/></svg><span>ADVERTISEMENT</span></div>
  <div class="ad two"><svg width="75" height="70" viewBox="0 0 75 70"><path d="M0 0L75 70M75 0L0 70" stroke="#e3e5e8" stroke-width=".8"/></svg><span>ADVERTISEMENT</span></div>

  <div class="topics-band"></div>

  <div class="topic-card c1">
    <div class="thumb" role="img" aria-label="Banknotes being counted"></div>
    <span class="icon"><svg width="7" height="7" viewBox="0 0 7 7"><path d="M1 6.5h5.5" stroke="#1a73c1" stroke-width=".7"/><rect x="1.3" y="4" width="1" height="2.2" fill="#1a73c1"/><rect x="3" y="3" width="1" height="3.2" fill="#1a73c1"/><rect x="4.7" y="2" width="1" height="4.2" fill="#1a73c1"/><path d="M1 3.2 3 1.8 4.4 2.4 6.2.6" fill="none" stroke="#1a73c1" stroke-width=".6"/></svg></span>
    <h3>Value vs. Growth</h3>
    <p>Nam libero tempore, cum soluta nobis est eligendi optio cumque nihil impedit</p>
  </div>
  <div class="topic-card c2">
    <div class="thumb" role="img" aria-label="Glowing rising bar chart"></div>
    <span class="icon"><svg width="7" height="7" viewBox="0 0 7 7"><path d="M1 6.5h5.5" stroke="#1a73c1" stroke-width=".7"/><rect x="1.3" y="4" width="1" height="2.2" fill="#1a73c1"/><rect x="3" y="3" width="1" height="3.2" fill="#1a73c1"/><rect x="4.7" y="2" width="1" height="4.2" fill="#1a73c1"/><path d="M1 3.2 3 1.8 4.4 2.4 6.2.6" fill="none" stroke="#1a73c1" stroke-width=".6"/></svg></span>
    <h3>Basics</h3>
    <p>Nam libero tempore, cum soluta nobis est eligendi optio cumque nihil impedit</p>
  </div>
  <div class="topic-card c3">
    <div class="thumb" role="img" aria-label="Office desk with a laptop and printed charts"></div>
    <span class="icon"><svg width="7" height="7" viewBox="0 0 7 7"><path d="M1 6.5h5.5" stroke="#1a73c1" stroke-width=".7"/><rect x="1.3" y="4" width="1" height="2.2" fill="#1a73c1"/><rect x="3" y="3" width="1" height="3.2" fill="#1a73c1"/><rect x="4.7" y="2" width="1" height="4.2" fill="#1a73c1"/><path d="M1 3.2 3 1.8 4.4 2.4 6.2.6" fill="none" stroke="#1a73c1" stroke-width=".6"/></svg></span>
    <h3>Global Investments</h3>
    <p>Nam libero tempore, cum soluta nobis est eligendi optio cumque nihil impedit</p>
  </div>
  <div class="topic-card c4">
    <div class="thumb" role="img" aria-label="Small model house with a red roof beside a set of keys"></div>
    <span class="icon"><svg width="7" height="7" viewBox="0 0 7 7"><path d="M1 6.5h5.5" stroke="#1a73c1" stroke-width=".7"/><rect x="1.3" y="4" width="1" height="2.2" fill="#1a73c1"/><rect x="3" y="3" width="1" height="3.2" fill="#1a73c1"/><rect x="4.7" y="2" width="1" height="4.2" fill="#1a73c1"/><path d="M1 3.2 3 1.8 4.4 2.4 6.2.6" fill="none" stroke="#1a73c1" stroke-width=".6"/></svg></span>
    <h3>Where to Invest</h3>
    <p>Nam libero tempore, cum soluta nobis est eligendi optio cumque nihil impedit</p>
  </div>

  <footer class="site-footer">
    <span>© 2019 Harbor Crest Capital</span><span class="dot"></span><span>All rights reserved</span><span class="dot"></span><span>48 Meridian Row, Suite 9, Lakeport, IL 60000</span><span class="dot"></span><span>(555) 010 - 2040</span>
  </footer>
</section>

</body>
</html>
```